concept design for a website homepage

Hi, we are looking for a design for Homepage for our childcare centre
We want something really progressive, edgy, modern and premium. We want this website to standout but not cluttered. We only need a Homepage concept design for the below measurements.
1366 Wx768 H
The call to action is join our community
We like the idea of a split screen
Divided into 4 sections screen with the below
Locations and Enrolments
Tandel
Careers
Partnerships
We like angles and shapes, particularly triangles in the designs in the attached examples.
Our company font is Hands of Sean
Have attached some designs that we like the look and feel of and some of our designs from our flyers and some images to use, you don't need to choose all the images, just whatever works with your design.
We have a STEM focus at our centres so something sciency would be great.
Consider in the design will be viewed on desktop and mobile phones
1 page

```html
<!DOCTYPE html>
<html lang="en">
<head>
<meta charset="utf-8">
<title>Sunbeam Hill — Homepage</title>
<link href="https://fonts.googleapis.com/css2?family=Gochi+Hand&family=Jost:wght@400;500;600&family=Roboto:wght@500&display=swap" rel="stylesheet">
<style>
  :root{
    --page:#03202b;
    --shade:#050506;
    --title:#8e8e8e;
    --more:#6a661c;
    --cta:#fff200;
    --ink:#000;
    --foot:#39505a;
    --icon:#2f4850;
    --icon-bg:#0b2a35;
  }
  *{margin:0;padding:0;box-sizing:border-box}
  html,body{width:1200px;height:675px;overflow:hidden;background:var(--page)}
  .page{position:relative;width:1200px;height:675px;font-family:"Roboto",sans-serif}
  .hero{position:absolute;left:33px;top:65px;width:1131px;height:523px;display:flex}
  .panel{position:relative;height:100%;overflow:hidden}
  .panel--locations{width:264px;background:
      radial-gradient(ellipse 70% 45% at 55% 30%,rgba(120,96,40,.55),transparent 70%),
      radial-gradient(ellipse 60% 40% at 30% 75%,rgba(40,60,58,.6),transparent 70%),
      linear-gradient(165deg,#3a2f17 0%,#2a2414 45%,#182022 100%)}
  .panel--careers{width:298px;background:
      radial-gradient(ellipse 30% 45% at 30% 45%,rgba(110,110,115,.45),transparent 70%),
      radial-gradient(ellipse 28% 30% at 75% 45%,rgba(95,95,100,.35),transparent 70%),
      radial-gradient(ellipse 80% 30% at 50% 90%,rgba(95,78,50,.6),transparent 75%),
      linear-gradient(180deg,#0e0f12 0%,#1a1a1d 50%,#2b2619 100%)}
  .panel--tandel{width:275px;background:
      radial-gradient(ellipse 60% 30% at 55% 28%,rgba(40,50,60,.55),transparent 70%),
      radial-gradient(ellipse 50% 25% at 40% 70%,rgba(30,34,40,.6),transparent 70%),
      linear-gradient(180deg,#0a0d12 0%,#0f1116 60%,#0b0c0e 100%)}
  .panel--partner{width:294px;background:
      radial-gradient(ellipse 60% 25% at 50% 30%,rgba(40,48,58,.55),transparent 70%),
      radial-gradient(ellipse 55% 30% at 60% 82%,rgba(140,70,30,.65),transparent 72%),
      radial-gradient(ellipse 35% 18% at 85% 88%,rgba(120,40,30,.5),transparent 70%),
      linear-gradient(180deg,#0b0f14 0%,#121418 42%,#3a2616 75%,#4a3018 100%)}
  .shade-box{position:absolute;left:36px;top:383px;width:239px;height:140px;background:var(--shade)}
  .panel-title{position:absolute;font-family:"Gochi Hand",cursive;color:var(--title);font-size:36px;line-height:31px;white-space:nowrap}
  .read-more{position:absolute;font-weight:500;font-size:13px;line-height:15px;color:var(--more)}
  .brand{position:absolute;left:78px;top:20px;width:129px;height:121px;background:#0d3a40;display:flex;align-items:center;justify-content:center;text-align:center;font-family:"Gochi Hand",cursive;font-size:24px;line-height:24px;color:#6b5f16}
  .social{position:absolute;top:26px;left:935px;display:flex;gap:11px}
  .social span{width:22px;height:22px;border-radius:50%;background:var(--icon-bg);border:2px solid var(--icon)}
  .tools{position:absolute;top:26px;left:1088px}
  .cta{position:absolute;left:636px;top:241px;width:564px;height:149px;background:var(--cta);border-radius:20px 0 0 20px}
  .cta-side{position:absolute;left:38px;top:16px;width:16px;height:122px;writing-mode:vertical-rl;transform:rotate(180deg);font-weight:500;font-size:12px;line-height:16px;color:var(--ink);text-align:center;white-space:nowrap}
  .cta-arrow{position:absolute;left:20px;top:14px}
  .cta-head{position:absolute;left:68px;top:6px;font-family:"Gochi Hand",cursive;font-size:50px;line-height:52px;color:var(--ink);letter-spacing:1px}
  .cta-sub{position:absolute;left:70px;top:58px;font-family:"Jost",sans-serif;font-weight:600;font-size:25px;line-height:28px;letter-spacing:1.5px;color:var(--ink);white-space:nowrap}
  .cta-meta{position:absolute;left:71px;top:90px;font-family:"Jost",sans-serif;font-size:17.5px;line-height:22px;color:var(--ink);white-space:nowrap}
  .cta-note{position:absolute;left:71px;top:113px;font-family:"Jost",sans-serif;font-size:15px;line-height:19px;color:var(--ink);white-space:nowrap}
  .cta-button{position:absolute;left:456px;top:6px;width:61px;height:137px;background:var(--ink);display:flex;align-items:center;justify-content:center}
  .cta-button span{writing-mode:vertical-rl;transform:rotate(180deg);font-family:"Gochi Hand",cursive;font-size:27px;color:#fff;letter-spacing:2px;white-space:nowrap}
  .footer-nav{position:absolute;left:34px;top:641px;font-weight:500;font-size:14.5px;color:var(--foot);word-spacing:1px;white-space:nowrap}
  .footer-nav b{font-weight:500;margin:0 6px}
  .copyright{position:absolute;right:40px;top:643px;font-weight:500;font-size:14.5px;color:var(--foot);white-space:nowrap}
</style>
</head>
<body>
<main class="page">
  <section class="hero">
    <div class="panel panel--locations" role="img" aria-label="Child in a hard hat exploring a science classroom">
      <div class="panel-title" style="left:22px;top:415px">Location and<br>Enrolments</div>
      <div class="read-more" style="left:25px;top:489px">Read more</div>
    </div>
    <div class="panel panel--careers" role="img" aria-label="Children in lab coats gathered at a science table">
      <div class="panel-title" style="left:176px;top:235px">Career</div>
      <div class="read-more" style="left:177px;top:270px">Read more</div>
    </div>
    <div class="panel panel--tandel" role="img" aria-label="Dimly lit planetarium-style learning room">
      <div class="shade-box"></div>
      <div class="panel-title" style="left:134px;top:448px">Tandel</div>
      <div class="read-more" style="left:138px;top:489px">Read more</div>
    </div>
    <div class="panel panel--partner" role="img" aria-label="Colourful play space with small tables and soft seats">
      <div class="panel-title" style="left:123px;top:34px">Partnership</div>
      <div class="read-more" style="left:127px;top:69px">Read more</div>
    </div>
  </section>

  <div class="brand">Sunbeam<br>Hill</div>

  <nav class="social" aria-label="Social links"><span></span><span></span><span></span><span></span></nav>
  <svg class="tools" width="60" height="24" viewBox="0 0 60 24" aria-hidden="true">
    <circle cx="7" cy="9" r="5" fill="none" stroke="var(--icon)" stroke-width="2.5"/>
    <line x1="11" y1="13" x2="19" y2="19" stroke="var(--icon)" stroke-width="3.5" stroke-linecap="round"/>
    <rect x="43" y="2" width="20" height="3.5" fill="var(--icon)"/>
    <rect x="43" y="10" width="20" height="3.5" fill="var(--icon)"/>
    <rect x="43" y="18" width="20" height="3.5" fill="var(--icon)"/>
  </svg>

  <aside class="cta">
    <svg class="cta-arrow" width="12" height="16" viewBox="0 0 12 16" aria-hidden="true"><path d="M3 3 L8 8 L3 13" fill="none" stroke="#000" stroke-width="2.6"/></svg>
    <div class="cta-side">Join our Community</div>
    <div class="cta-head">Join Our</div>
    <div class="cta-sub">LAKEVIEW COMMUNITY</div>
    <div class="cta-meta">6 weeks - 6 Years 17:00 am - 6:00 pm</div>
    <div class="cta-note">Australian and family - owned and operated service</div>
    <a class="cta-button"><span>Join Now</span></a>
  </aside>

  <nav class="footer-nav">Home<b>|</b>Locations and Enrolments<b>|</b>Tandel<b>|</b>Careers<b>|</b>Partnerships</nav>
  <div class="copyright">Copyright 2022-23, sunbeamhill.com. All Rights Reserved.</div>
</main>
</body>
</html>
```